New therapy private practice needs a 2 sided postcard announcing location and services

We need a postcard sized card that is TWO SIDED and shares our new location and services offered. (new location is 3842. W. 58th #2300 in Tulsa, OK 74152) Name of the therapy business is "Bright Path! Counseling". Services offered include individual, marriage, family and group counseling. My phone number to place on the card is (918) 555-0143 and someone can call to schedule a free 20 minute consultation at that number.

These cards will also be mailed in an enclosed envelope or placed in welcome baskets as a marketing tool with possible referral sources like churches, doctors, and lawyers. (That means there does not have to be a space for an address or stamp to mail to. Full use of both sides of the card is important) We would like to see designs that use softer colors such as blue, purples, or greens. The final design should communicate a feeling of peace and hope and a sense of freshness and approachability. Incorporating a tag line such as..... "where you'll find hope!" would be good. My website is www.brightpathnow.example and extra info about my practice is on there. It is important my credentials are listed on the postcard. Lena Marsh Voight, LPC-S, LMFT

I am not looking for a bunch of "box looking pictures". The pictures I am uploading are for ideas, although my logo and picture should be used. I like the type of picture I have on my homepage of my website with the quote "Let your hopes, not your fears shape your future"

Target Market(s)

Primarily women and couples looking for counseling for relationships, anxiety, depression, or life transitions.

Font styles to use
Serif
Script

Colors
3276b5
85acd3
86cfc6
33b8a4
cadf82
876aae
9bcb3c

Requirements
Must have
• My picture, address, website, and phone number as well as my logo.
• Address is: 3842 W. 58th Street #2300 Tulsa, OK 74152
• Web: www.brightpathnow.example
• Email: lena@brightpathnow.example
• Phone: (918) 555-0143
• "Hope anchors the soul" - Heb. 6:19
• On my website, I have a 2 minute video of myself. This may be helpful to watch in getting a "feel" for my counseling practice.
• Services Provided: ANXIETY | DEPRESSION | LIFE TRANSITIONS | MARRIAGE COUNSELING | SEPARATION AND DIVORCE | WOMEN’S ISSUES | ADDICTIONS AND INFIDELITY | PARENT/CHILD RELATIONSHIPS | FAMILY CONFLICT | TRAUMA/GRIEF AND LOSS
Nice to have
• A combination of print and script would be nice. A feeling of tranquility and hope
• I would like to have the statement at the bottom of the card.... " It is my desire for you to discover that no matter the situation you are currently going through….. there’s hope!"
• It would also be nice to have a small area that says: Lena is a graduate of Western Calloway College and has been in private practice for 11 years. She is a regular monthly co-host on the Meadow Broadcast Group at 97.3 FM
Should not have
• Heavy bold or abrasive feel

```html
<!DOCTYPE html>
<html lang="en">
<head>
<meta charset="utf-8">
<title>Bright Path! Counseling – Postcard</title>
<link rel="stylesheet" href="https://fonts.googleapis.com/css2?family=Days+One&family=Montserrat:wght@800&family=Open+Sans:wght@600;700&display=swap">
<style>
  :root {
    --page: #e6e8e7;
    --card-light: #f1f6f3;
    --card-mist: #d6e6e1;
    --leaf: #4e8a3a;
    --ink: #141414;
    --white: #ffffff;
    --photo-warm: #d99a3a;
    --photo-green: #7fa06a;
  }
  * { box-sizing: border-box; margin: 0; padding: 0; }
  html, body { width: 1200px; height: 1070px; overflow: hidden; background: var(--page); }
  body { position: relative; font-family: "Open Sans", sans-serif; }

  .postcard {
    position: absolute; left: 230px; width: 740px; height: 505px;
    background: linear-gradient(135deg, var(--card-light) 0%, var(--card-mist) 100%);
    overflow: hidden; box-shadow: 0 4px 14px rgba(0,0,0,.18);
  }
  .postcard--front { top: 20px; }
  .postcard--back { top: 545px; }
  .postcard__shapes { position: absolute; inset: 0; }

  .radio-note {
    position: absolute; left: 40px; top: 318px; width: 340px;
    color: var(--white); font-weight: 600; font-size: 14px; line-height: 1.3; text-align: center;
  }

  .brand {
    position: absolute; color: var(--leaf); font-family: "Open Sans", sans-serif;
    font-weight: 700; text-align: center; line-height: 1.05;
  }
  .brand__mark {
    display: inline-block; width: 26px; height: 26px; border-radius: 50%;
    background: var(--leaf); vertical-align: middle; margin-right: 10px;
  }
  .postcard--front .brand { left: 460px; top: 95px; width: 270px; font-size: 34px; }
  .postcard--back .brand { left: 400px; top: 40px; width: 320px; font-size: 30px; }

  .cta {
    position: absolute; font-family: "Days One", sans-serif; text-align: center;
    color: var(--ink); line-height: 1.25; white-space: nowrap; font-weight: 400;
  }
  .cta__accent { color: var(--leaf); }
  .postcard--front .cta { left: 432px; top: 240px; width: 300px; font-size: 25px; }
  .postcard--back .cta { left: 395px; top: 140px; width: 330px; font-size: 27px; }

  .contact {
    position: absolute; left: 0; right: 0; bottom: 14px; padding: 0 10px;
    color: var(--white); text-align: center; white-space: nowrap;
  }
  .contact__address { font-weight: 700; font-size: 18px; }
  .contact__lines { font-weight: 700; font-size: 17px; margin-top: 2px; }
  .contact__tagline { font-weight: 600; font-size: 12px; margin-top: 6px; }

  .issues { position: absolute; left: 40px; top: 40px; width: 350px; }
  .issues__title {
    font-family: "Montserrat", sans-serif; font-weight: 800; font-size: 20px;
    color: var(--ink); margin-bottom: 8px;
  }
  .issues__list { list-style: none; }
  .issues__item {
    font-family: "Montserrat", sans-serif; font-weight: 800; font-size: 15.5px;
    color: var(--leaf); line-height: 1.45; display: flex; align-items: center; gap: 12px;
    white-space: nowrap;
  }
  .issues__arrow { width: 14px; height: 12px; flex: none; }
</style>
</head>
<body>

<section class="postcard postcard--front" aria-label="Postcard front">
  <svg class="postcard__shapes" width="740" height="505" viewBox="0 0 740 505">
    <defs>
      <clipPath id="portrait-clip"><circle cx="205" cy="140" r="240"/></clipPath>
      <linearGradient id="portrait-tone" x1="0" y1="0" x2="1" y2="1">
        <stop offset="0" stop-color="#d99a3a"/>
        <stop offset="1" stop-color="#7fa06a"/>
      </linearGradient>
    </defs>
    <g clip-path="url(#portrait-clip)">
      <rect x="0" y="0" width="460" height="300" fill="url(#portrait-tone)" role="img" aria-label="Portrait photo of counselor Lena outdoors with autumn trees behind her"/>
      <rect x="0" y="300" width="460" height="100" fill="#141414"/>
    </g>
    <circle cx="205" cy="140" r="243" fill="none" stroke="#4e8a3a" stroke-width="5"/>
    <circle cx="205" cy="140" r="248" fill="none" stroke="#141414" stroke-width="4"/>
    <path d="M0 395 Q370 400 740 445 L740 505 L0 505 Z" fill="#4e8a3a"/>
    <path d="M0 395 Q370 400 740 445" fill="none" stroke="#141414" stroke-width="5"/>
  </svg>

  <p class="radio-note">Lena can be heard monthly on the<br>Meadow Broadcast Group<br>at 97.3 FM</p>

  <div class="brand"><span class="brand__mark"></span>Bright Path!<br>Counseling</div>

  <h2 class="cta">CALL TO SCHEDULE<br><span class="cta__accent">A FREE 20 MINUTE</span><br>CONSULTATION</h2>

  <div class="contact">
    <p class="contact__address">3842 W. 58th Street #2300 Tulsa, OK 74152</p>
    <p class="contact__lines">www.brightpathnow.example | lena@brightpathnow.example | (918) 555-0143</p>
    <p class="contact__tagline">It is my desire for you to discover that no matter the situation you are currently going through..... there’s a bright path!</p>
  </div>
</section>

<section class="postcard postcard--back" aria-label="Postcard back">
  <svg class="postcard__shapes" width="740" height="505" viewBox="0 0 740 505" aria-hidden="true">
    <path d="M0 395 Q370 400 740 345 L740 505 L0 505 Z" fill="#4e8a3a"/>
    <path d="M0 395 Q370 400 740 345" fill="none" stroke="#141414" stroke-width="5"/>
  </svg>

  <div class="issues">
    <h3 class="issues__title">ISSUES SERVED:</h3>
    <ul class="issues__list">
      <li class="issues__item"><svg class="issues__arrow" viewBox="0 0 14 12"><path d="M0 0 L14 6 L0 12 L4 6 Z" fill="#141414"/></svg>ANXIETY</li>
      <li class="issues__item"><svg class="issues__arrow" viewBox="0 0 14 12"><path d="M0 0 L14 6 L0 12 L4 6 Z" fill="#141414"/></svg>DEPRESSION</li>
      <li class="issues__item"><svg class="issues__arrow" viewBox="0 0 14 12"><path d="M0 0 L14 6 L0 12 L4 6 Z" fill="#141414"/></svg>LIFE TRANSITIONS</li>
      <li class="issues__item"><svg class="issues__arrow" viewBox="0 0 14 12"><path d="M0 0 L14 6 L0 12 L4 6 Z" fill="#141414"/></svg>MARRIAGE COUNSELING</li>
      <li class="issues__item"><svg class="issues__arrow" viewBox="0 0 14 12"><path d="M0 0 L14 6 L0 12 L4 6 Z" fill="#141414"/></svg>SEPARATION AND DIVORCE</li>
      <li class="issues__item"><svg class="issues__arrow" viewBox="0 0 14 12"><path d="M0 0 L14 6 L0 12 L4 6 Z" fill="#141414"/></svg>WOMEN’S ISSUES</li>
      <li class="issues__item"><svg class="issues__arrow" viewBox="0 0 14 12"><path d="M0 0 L14 6 L0 12 L4 6 Z" fill="#141414"/></svg>ADDICTIONS AND INFIDELITY</li>
      <li class="issues__item"><svg class="issues__arrow" viewBox="0 0 14 12"><path d="M0 0 L14 6 L0 12 L4 6 Z" fill="#141414"/></svg>PARENT/CHILD RELATIONSHIPS</li>
      <li class="issues__item"><svg class="issues__arrow" viewBox="0 0 14 12"><path d="M0 0 L14 6 L0 12 L4 6 Z" fill="#141414"/></svg>FAMILY CONFLICT</li>
      <li class="issues__item"><svg class="issues__arrow" viewBox="0 0 14 12"><path d="M0 0 L14 6 L0 12 L4 6 Z" fill="#141414"/></svg>TRAUMA/GRIEF AND LOSS</li>
    </ul>
  </div>

  <div class="brand"><span class="brand__mark"></span>Bright Path! Counseling</div>

  <h2 class="cta">CALL TO SCHEDULE<br><span class="cta__accent">A FREE 20 MINUTE</span><br>CONSULTATION</h2>

  <div class="contact">
    <p class="contact__address">3842 W. 58th Street #2300 Tulsa, OK 74152</p>
    <p class="contact__lines">www.brightpathnow.example | lena@brightpathnow.example | (918) 555-0143</p>
    <p class="contact__tagline">It is my desire for you to discover that no matter the situation you are currently going through..... there’s a bright path!</p>
  </div>
</section>

</body>
</html>
```